The Gemstone Craft Studio Sales Business Card

The goal of this project is to create a interactive & effective business card design for SALES purposes with the intention to get customer on to our website and make a purchase or contact us about a product or service.
Website: WWW.RINGFORGEHUB.COM
GoogleMyBusiness: https://g.page/RingForgeHUB?gm
Facebook & Instagram: @THEGEMSTONECRAFTSTUDIO
Phone # & Text Message & Whatsapp Message: +1(555) 418-0293
Email: HELLO@RINGFORGEHUB.COM
Location: 4872 Brambleton Avenue Suite 512 Millbrook, OR
(It would be necessary to have the appropriate ticker/icon for each social media platform as well as the location ticker and phone / messaging icons instead of spelling the words out.)
It is important to have the company logo and details but with an emphasis toward website. Feel free to also completely make one design your way and completely custom as you feel best.
The Gemstone Craft Studio is a Provider of Luxury Goods & Services such as: Custom Jewelry Design, Jewelry Repairs & Cleaning, Designer Jewelry, Luxury Gifts, 24 Karat Gold, 22 Karat Gold Jewelry, Diamond Jewelry, Insured Jewelry Appraisals, Loose Gemstones & Diamonds, Supporting Sustainability
Target Market(s)
People looking to invest in precious metals and gemstones as well as people looking to find a gift for a loved one for a special occasion. Customers looking to Custom Design Jewelry.
Contact Information for Business Card
Font styles to use
Other font styles liked:
- w.e you want
Colors
Designer to choose colors to be used in the design.
Requirements
Must have
- Website: WWW.RINGFORGEHUB.COM
- GoogleMyBusiness: https://g.page/RingForgeHUB?gm
- Facebook & Instagram: @THEGEMSTONECRAFTSTUDIO
- Phone # & Text Message & Whatsapp Message: +1(555) 418-0293
- Email: HELLO@RINGFORGEHUB.COM
- Location: 4872 Brambleton Avenue Suite 512 Millbrook, OR
- (It would be necessary to have the appropriate ticker/icon for each social media platform as well as the location ticker and phone / messaging icons instead of spelling the words out.)
- It is important to have the company logo and details but with an emphasis toward website. Feel free to also completely make one design your way and completely custom as you feel best.
Nice to have
- The Gemstone Craft Studio is a Provider of Luxury Goods & Services such as: Custom Jewelry Design, Jewelry Repairs & Cleaning, Designer Jewelry, Luxury Gifts, 24 Karat Gold, 22 Karat Gold Jewelry, Diamond Jewelry, Insured Jewelry Appraisals, Loose Gemstones & Diamonds, Supporting Sustainability

```html
<!DOCTYPE html>
<html lang="en">
<head>
<meta charset="utf-8">
<title>The Gemstone Craft Studio – Business Card</title>
<link rel="stylesheet" href="https://fonts.googleapis.com/css2?family=Open+Sans:wght@400;600;700&display=swap">
<style>
  :root {
    --bg: #2c2e33;
    --paper: #ffffff;
    --brand-red: #e41f26;
    --brand-yellow: #f6c631;
    --ink: #1b1b1b;
    --pill: #3a3a3a;
  }
  * { box-sizing: border-box; margin: 0; padding: 0; }
  html, body { width: 1200px; height: 900px; overflow: hidden; }
  body {
    background: var(--bg);
    font-family: "Open Sans", Arial, sans-serif;
    position: relative;
  }
  .card {
    position: absolute;
    width: 540px;
    height: 309px;
    background: var(--paper);
    box-shadow: 0 12px 30px rgba(0,0,0,.45);
    overflow: hidden;
  }
  .card--front { left: 40px; top: 296px; }
  .card--back { left: 620px; top: 296px; }
  .card__shapes { position: absolute; inset: 0; }

  /* front */
  .brand {
    position: absolute;
    left: 0; width: 222px; top: 0; height: 309px;
    display: flex; flex-direction: column; align-items: center; justify-content: center;
    gap: 14px;
  }
  .brand__dot { width: 40px; height: 40px; border-radius: 50%; background: var(--brand-yellow); }
  .brand__name {
    color: var(--brand-red);
    font-weight: 700;
    font-size: 21px;
    line-height: 1.15;
    text-align: center;
    letter-spacing: .5px;
  }
  .contact {
    position: absolute;
    left: 236px; right: 0;
    display: flex; align-items: center; justify-content: center; gap: 6px;
    color: #fff; font-size: 12px; font-weight: 600; white-space: nowrap;
  }
  .contact--gmb { top: 20px; }
  .contact--social { top: 50px; font-size: 12.5px; }
  .contact--phone { top: 174px; font-size: 13px; }
  .contact--mail { top: 204px; }
  .contact--address { top: 236px; font-size: 9.6px; }
  .contact svg { flex: none; }
  .icon-tile { width: 14px; height: 14px; border-radius: 3px; background: #fff; flex: none; }
  .icon-tile--round { border-radius: 50%; background: var(--brand-yellow); }
  .website {
    position: absolute;
    left: 276px; top: 125px; width: 250px; height: 30px;
    display: flex; align-items: center; justify-content: center;
    color: #fff; font-weight: 700; font-size: 16px; letter-spacing: .5px;
  }

  /* back */
  .about { position: absolute; left: 34px; right: 34px; top: 40px; color: var(--ink); }
  .about__title {
    font-size: 14.5px; font-weight: 600;
    padding-bottom: 8px; border-bottom: 2px solid var(--ink); margin-bottom: 10px;
  }
  .about__list { font-size: 12.5px; line-height: 1.6; font-weight: 600; }
  .back-brand {
    position: absolute; right: 60px; bottom: 40px;
    color: var(--brand-red); font-weight: 700; font-size: 17px; line-height: 1.15; text-align: center;
  }
</style>
</head>
<body>

<section class="card card--front" aria-label="Business card front">
  <svg class="card__shapes" width="540" height="309" viewBox="0 0 540 309" aria-hidden="true">
    <rect x="222" y="0" width="14" height="309" fill="var(--brand-yellow)"/>
    <rect x="236" y="0" width="304" height="309" fill="var(--brand-red)"/>
    <rect x="236" y="118" width="304" height="44" fill="var(--brand-yellow)"/>
    <rect x="250" y="124" width="280" height="32" rx="16" fill="var(--pill)"/>
    <circle cx="266" cy="140" r="12" fill="#fff"/>
    <circle cx="266" cy="140" r="8" fill="none" stroke="var(--pill)" stroke-width="1.6"/>
    <ellipse cx="266" cy="140" rx="3.5" ry="8" fill="none" stroke="var(--pill)" stroke-width="1.4"/>
    <line x1="258" y1="140" x2="274" y2="140" stroke="var(--pill)" stroke-width="1.4"/>
  </svg>

  <div class="brand">
    <span class="brand__dot"></span>
    <p class="brand__name">Gemstone<br>Craft Studio</p>
  </div>

  <p class="contact contact--gmb"><span class="icon-tile"></span>https://g.page/RingForgeHUB?gm</p>
  <p class="contact contact--social"><span class="icon-tile"></span><span class="icon-tile"></span>@THEGEMSTONECRAFTSTUDIO</p>
  <p class="website">WWW.RINGFORGEHUB.COM</p>
  <p class="contact contact--phone">
    <svg width="14" height="14" viewBox="0 0 24 24" aria-hidden="true"><path fill="#fff" d="M6.6 10.8a15 15 0 0 0 6.6 6.6l2.2-2.2c.3-.3.7-.4 1-.2 1.1.4 2.3.6 3.6.6.6 0 1 .4 1 1V20c0 .6-.4 1-1 1A17 17 0 0 1 3 4c0-.6.4-1 1-1h3.5c.6 0 1 .4 1 1 0 1.3.2 2.5.6 3.6.1.3 0 .7-.2 1z"/></svg>
    <svg width="14" height="14" viewBox="0 0 24 24" aria-hidden="true"><path fill="#fff" d="M3 4h18v12H8l-5 4z"/></svg>
    <span class="icon-tile icon-tile--round"></span>
    +1(555) 418-0293
  </p>
  <p class="contact contact--mail">
    <svg width="15" height="12" viewBox="0 0 24 18" aria-hidden="true"><rect x="1" y="1" width="22" height="16" rx="2" fill="var(--brand-yellow)"/><path d="M2 2l10 8 10-8" fill="none" stroke="var(--brand-red)" stroke-width="2"/></svg>
    HELLO@RINGFORGEHUB.COM
  </p>
  <p class="contact contact--address">
    <svg width="11" height="14" viewBox="0 0 20 26" aria-hidden="true"><path fill="#1f8fe0" d="M10 0a9 9 0 0 0-9 9c0 7 9 17 9 17s9-10 9-17a9 9 0 0 0-9-9z"/><circle cx="10" cy="9" r="3.5" fill="#fff"/></svg>
    4872 Brambleton Avenue Suite 512 Millbrook, OR
  </p>
</section>

<section class="card card--back" aria-label="Business card back">
  <div class="about">
    <h1 class="about__title">The Gemstone Craft Studio is a Provider of Luxury Goods &amp; Services such as:</h1>
    <p class="about__list">Custom Jewelry Design, Jewelry Repairs &amp; Cleaning, Designer Jewelry, Luxury Gifts, 24 Karat Gold, 22 Karat Gold Jewelry, Diamond Jewelry, Insured Jewelry Appraisals, Loose Gemstones &amp; Diamonds, Supporting Sustainability.</p>
  </div>
  <p class="back-brand">Gemstone<br>Craft Studio</p>
</section>

</body>
</html>
```